Graphically Innovative Birthday Card

We need a new corporate birthday and Christmas card. Benevora is a faith-based charitable foundation based in Ontario, Canada. We partner with the Reformed Covenant Fellowship of Canada to provide investment, fundraising support and gift planning services to individuals and congregations. We require design that reflect the Benevora brand, while embodying a tone and feel that represents the Christian faith without be overly symbolic. Attached is an example of the card developed in 2024 as a reference for the creative caliber and quality of design we hope to see in the new card. A full creative brief, including content copy is also attached, along with Benevora logo assets and brand guide.

Target Market(s)

See attached creative brief

Industry/Entity Type

Non profit (religious)

Font styles to use
Other font styles liked:
• Nunito Sans and Playfair Display - See attached brand guide

Requirements
Must have
• Brand colours - colour guide atttaced
Nice to have
• Innovative and creative. WOW us
Should not have
• Anything offensive or colours not relating to the brand

```html
<!DOCTYPE html>
<html lang="en">
<head>
<meta charset="utf-8">
<title>Benevora Birthday Card</title>
<link rel="stylesheet" href="https://fonts.googleapis.com/css2?family=Playfair+Display:ital,wght@0,400;0,600;0,700;1,700&display=swap">
<style>
  :root {
    --stage: #c3c4c6;
    --navy: #022d57;
    --leaf: #6a8f3c;
    --leaf-soft: #7a9a55;
    --accent: #8fb356;
    --ink: #0f2b52;
    --body: #4a4d50;
    --wash-top: #d9f0f5;
    --wash-mid: #e7f5f3;
    --wash-bottom: #ebf4de;
    --foliage: #5d9a4c;
    --white: #ffffff;
  }
  * { box-sizing: border-box; margin: 0; padding: 0; }
  html, body { width: 777px; height: 1200px; overflow: hidden; }
  body {
    background: var(--stage);
    font-family: "Playfair Display", Georgia, serif;
    position: relative;
  }
  .spread {
    position: absolute;
    box-shadow: 0 6px 10px rgba(0,0,0,0.35);
    overflow: hidden;
  }
  .spread--outside { left: 57px; top: 77px; width: 663px; height: 473px; display: flex; }
  .spread--inside {
    left: 59px; top: 610px; width: 659px; height: 470px;
    background: linear-gradient(175deg, var(--wash-top) 0%, var(--wash-mid) 45%, var(--wash-bottom) 100%);
  }

  /* Back cover */
  .back-cover { width: 331px; height: 100%; background: var(--navy); position: relative; }
  .brand-block {
    position: absolute; left: 0; right: 0; top: 376px;
    text-align: center; color: var(--white);
  }
  .brand-name {
    display: inline-flex; align-items: center; gap: 6px;
    font-size: 21px; font-weight: 700; line-height: 24px;
  }
  .brand-dot { width: 16px; height: 16px; border-radius: 50%; border: 2px solid var(--white); }
  .brand-tagline { font-size: 12px; font-weight: 600; line-height: 16px; margin-top: 6px; }
  .brand-url { font-size: 12px; font-weight: 600; line-height: 16px; margin-top: 3px; }
  .accent { color: var(--accent); }

  /* Front cover */
  .front-cover {
    flex: 1; height: 100%; position: relative;
    background: linear-gradient(175deg, var(--wash-top) 0%, var(--wash-mid) 50%, var(--wash-bottom) 100%);
  }
  .wreath { position: absolute; left: 1px; top: 79px; width: 320px; height: 320px; }
  .front-title {
    position: absolute; left: 0; right: 12px; top: 182px;
    text-align: center; color: var(--leaf);
    font-style: italic; font-weight: 700; font-size: 43.5px; line-height: 50px;
  }

  /* Inside */
  .foliage-corner { position: absolute; }
  .foliage-corner--top-left { left: 0; top: 0; width: 270px; height: 290px; }
  .foliage-corner--bottom-right { right: 0; bottom: 0; width: 280px; height: 170px; }

  .verse {
    position: absolute; left: 25px; width: 260px; top: 179px;
    text-align: center; color: var(--ink);
  }
  .verse-text { font-size: 16px; font-weight: 600; line-height: 19.2px; }
  .verse-text .mark { color: var(--leaf); font-size: 22px; font-weight: 700; line-height: 0; }
  .verse-ref { color: var(--leaf-soft); font-size: 16px; line-height: 20px; margin-top: 30px; }

  .greeting {
    position: absolute; left: 362px; width: 270px; top: 106px;
    text-align: center;
  }
  .greeting-title { color: var(--leaf); font-weight: 700; font-size: 43px; line-height: 49px; }
  .greeting-sub { color: var(--ink); font-weight: 600; font-size: 19px; line-height: 24px; margin-top: 6px; }
  .greeting-body { color: var(--body); font-size: 14.8px; line-height: 20.7px; margin-top: 12px; }
</style>
</head>
<body>
  <section class="spread spread--outside">
    <div class="back-cover">
      <div class="brand-block">
        <div class="brand-name"><span class="brand-dot"></span>Benevora</div>
        <p class="brand-tagline">Faith Guiding <span class="accent">Giving</span></p>
        <p class="brand-url">benevora<span class="accent">.ca</span></p>
      </div>
    </div>
    <div class="front-cover">
      <svg class="wreath" viewBox="0 0 320 320" role="img" aria-label="Watercolour eucalyptus wreath with a thin gold ring">
        <defs>
          <radialGradient id="wreathTone" cx="50%" cy="50%" r="50%">
            <stop offset="70%" stop-color="#6fa859" stop-opacity="0"/>
            <stop offset="84%" stop-color="#6fa859" stop-opacity="0.45"/>
            <stop offset="100%" stop-color="#6fa859" stop-opacity="0"/>
          </radialGradient>
        </defs>
        <circle cx="160" cy="160" r="158" fill="url(#wreathTone)"/>
      </svg>
      <h1 class="front-title">Happy<br>Birthday!</h1>
    </div>
  </section>

  <section class="spread spread--inside">
    <svg class="foliage-corner foliage-corner--top-left" viewBox="0 0 270 290" role="img" aria-label="Watercolour eucalyptus branches hanging from the corner">
      <defs>
        <radialGradient id="cornerTL" cx="0%" cy="0%" r="100%">
          <stop offset="0%" stop-color="#5d9a4c" stop-opacity="0.75"/>
          <stop offset="100%" stop-color="#5d9a4c" stop-opacity="0"/>
        </radialGradient>
      </defs>
      <rect width="270" height="290" fill="url(#cornerTL)"/>
    </svg>
    <svg class="foliage-corner foliage-corner--bottom-right" viewBox="0 0 280 170" role="img" aria-label="Watercolour eucalyptus leaves rising from the corner">
      <defs>
        <radialGradient id="cornerBR" cx="100%" cy="100%" r="100%">
          <stop offset="0%" stop-color="#5d9a4c" stop-opacity="0.75"/>
          <stop offset="100%" stop-color="#5d9a4c" stop-opacity="0"/>
        </radialGradient>
      </defs>
      <rect width="280" height="170" fill="url(#cornerBR)"/>
    </svg>

    <div class="verse">
      <p class="verse-text"><span class="mark">&ldquo;</span>For we are God&rsquo;s handiwork,<br>created in Christ Jesus to do<br>good works, which<br>God prepared in advance for<br>us to do. <span class="mark">&rdquo;</span></p>
      <p class="verse-ref">&mdash; Ephesians 2:10 NIV</p>
    </div>

    <div class="greeting">
      <h2 class="greeting-title">Happy<br>Birthday!</h2>
      <p class="greeting-sub">You are a gift to this world.</p>
      <p class="greeting-body">May your year ahead be<br>blessed with grace, love and<br>the kind of joy that<br>touches your soul.</p>
    </div>
  </section>
</body>
</html>
```